Plumtree Crate Society - New Website Design

Create a professional website for strawberries of the month club; a subscription box business that will INCLUDE dipped strawberries - some with sprinkles. Check out: http://www.orchardnook.com for examples. Our website URL will be www.PlumtreeCrateSociety.com
Please see wimplesack.com; fudgeguild.com and gruffcase.com for the concept I am after. The business has not been launched yet, I am currently in the pre-launch stage using a specialized landing page website, and so the time scale for developing my professional looking website is up to 1-2 weeks.
The webpage should have a fun feel and should match the style of the company logo at fudgeguild.com or gruffcase.com. The pages to include are 'Home', 'About us' and 'Get Started'
Thank you and good luck!

```html
<!DOCTYPE html>
<html lang="en">
<head>
<meta charset="utf-8">
<title>Plumtree Crate Society</title>
<link href="https://fonts.googleapis.com/css2?family=Lato:wght@400;700;900&family=Open+Sans:wght@400&family=Roboto:wght@400;500;700&family=Merriweather:wght@400;700&display=swap" rel="stylesheet">
<style>
:root{
  --white:#ffffff;
  --ink:#2b2b2b;
  --text:#555555;
  --muted:#777777;
  --line:#e6e6e6;
  --footer-bg:#f6f6f6;
  --red:#e30f14;
  --pink:#e58a98;
  --dark-btn:#333333;
  --input-bg:#f3f3f3;
}
*{box-sizing:border-box;margin:0;padding:0}
html,body{width:1200px;height:2546px;overflow:hidden;background:var(--white)}
body{position:relative;font-family:'Open Sans',sans-serif;color:var(--text)}
.abs{position:absolute}
.photo{position:absolute;display:block}

/* hero */
.hero{left:0;top:0;width:1200px;height:591px;
  background:radial-gradient(circle at 30% 40%,#c6201c 0,#8f1010 35%,#3c0506 75%),#6a0a0a}
.hero::after{content:"";position:absolute;inset:0;
  background:radial-gradient(circle at 12% 18%,rgba(80,150,50,.55) 0,transparent 12%),
  radial-gradient(circle at 62% 52%,rgba(80,150,50,.5) 0,transparent 10%),
  radial-gradient(circle at 40% 3%,rgba(80,150,50,.5) 0,transparent 9%),
  radial-gradient(circle at 96% 30%,rgba(80,150,50,.45) 0,transparent 8%),
  rgba(0,0,0,.12)}
.brand{left:149px;top:15px;font-family:'Lato',sans-serif;font-weight:900;font-size:21px;color:var(--white);text-transform:uppercase;letter-spacing:.3px;z-index:2}
.nav{top:21px;font-family:'Roboto',sans-serif;font-weight:700;font-size:12px;color:var(--white);text-transform:uppercase;z-index:2}
.nav-icons{left:962px;top:16px;z-index:2;display:flex;gap:14px;align-items:center;color:var(--white);font:700 10px 'Roboto',sans-serif}
.hero-title{left:0;width:1200px;top:253px;text-align:center;font-family:'Lato',sans-serif;font-weight:700;font-size:50px;line-height:57px;color:var(--white);text-transform:uppercase;z-index:2}
.hero-btn{left:499px;top:385px;width:202px;height:46px;background:var(--red);color:var(--white);font:700 18px 'Lato',sans-serif;text-transform:uppercase;display:flex;align-items:center;justify-content:center;border-radius:2px;z-index:2}

/* grid photos */
.tile{width:297px;height:207px}
.macarons{background:linear-gradient(135deg,#f3ece2,#d9c7a8 55%,#e9e2d6)}
.pancake{background:linear-gradient(120deg,#f4f2ef 40%,#d89a5c 55%,#2f3448)}
.cookies{background:linear-gradient(160deg,#c9c6c3,#e8c89b 50%,#f1ede8)}
.citrus{background:linear-gradient(130deg,#f2e7e4,#e8a076 55%,#b95b2f)}
.teacup{background:linear-gradient(120deg,#b9584a,#f1e9e2 50%,#2f4a7a)}
.tray{background:linear-gradient(140deg,#2b3d5c,#3f9fb0 50%,#d46a6a)}
.drinks{background:linear-gradient(150deg,#5a4636,#c84a4a 50%,#e8d3b0)}
.parfait{background:linear-gradient(140deg,#f6f4f2,#f0d7d2 50%,#cf3e3e)}

/* sidebar */
.book{left:808px;top:626px;width:241px;height:333px;background:linear-gradient(160deg,#2c3548,#4b5670 50%,#c8874a 80%,#2c3548);border:1px solid #222}
.social-box{left:808px;top:972px;width:241px;height:72px;border:1px solid var(--line);display:flex;align-items:center;justify-content:center;gap:10px;font:700 9px 'Roboto',sans-serif;color:var(--ink)}
.cat{left:808px;width:241px}
.cakes{top:1056px;height:178px;background:linear-gradient(150deg,#e7d9d2,#efe3dc 40%,#5a2e25 80%)}
.fruits{top:1241px;height:179px;background:linear-gradient(140deg,#2b3d5c,#3f9fb0 50%,#d46a6a)}
.cat-label{position:absolute;left:50%;top:50%;transform:translate(-50%,-50%);background:var(--white);outline:1px solid var(--white);outline-offset:3px;border:1px solid #444;padding:4px 12px;font:400 10px 'Merriweather',serif;letter-spacing:2px;color:var(--ink)}
.newsletter{left:808px;top:1431px;width:241px;height:190px;border:1px solid var(--line);text-align:center}
.nl-head{position:absolute;top:24px;left:0;width:100%;font:700 10px 'Roboto',sans-serif;letter-spacing:2.5px;color:var(--pink)}
.nl-head::before,.nl-head::after{content:"";position:absolute;top:6px;width:34px;height:1px;background:var(--pink)}
.nl-head::before{left:32px}.nl-head::after{right:32px}
.nl-text{position:absolute;top:62px;left:0;width:100%;font:400 11px 'Merriweather',serif;color:var(--ink)}
.nl-input{position:absolute;left:17px;top:90px;width:205px;height:32px;background:var(--input-bg);font:400 10px 'Merriweather',serif;color:#bbb;display:flex;align-items:center;justify-content:center}
.nl-btn{position:absolute;left:17px;top:131px;width:205px;height:31px;background:var(--dark-btn);color:var(--white);font:700 11px 'Merriweather',serif;display:flex;align-items:center;justify-content:center}

/* featured post */
.feature{left:149px;top:1658px;width:900px;height:470px;background:linear-gradient(115deg,#f3efe9 0,#e6c27a 25%,#c24a3a 40%,#f4f3f1 60%,#f4f3f1 78%,#25324d 90%)}
.post-title{left:0;width:1200px;top:2146px;text-align:center;font:400 27px 'Lato',sans-serif;color:var(--ink);text-transform:uppercase}
.post-date{left:0;width:1200px;top:2185px;text-align:center;font:400 12px 'Lato',sans-serif;color:var(--muted);text-transform:uppercase}
.post-excerpt{left:270px;width:660px;top:2217px;text-align:center;font:400 17px/28px 'Open Sans',sans-serif;color:var(--muted)}

/* footer */
.footer{left:0;top:2335px;width:1200px;height:211px;background:var(--footer-bg)}
.f-col{position:absolute;top:31px;list-style:none;font:400 12px/24px 'Roboto',sans-serif;color:var(--ink)}
.pay{position:absolute;left:886px;top:31px;width:162px;font:700 11px 'Roboto',sans-serif;color:var(--ink)}
.pay-row{display:flex;justify-content:flex-end;gap:12px;height:33px;align-items:center}
.copyright{position:absolute;left:0;width:1200px;top:170px;text-align:center;font:400 11px 'Roboto',sans-serif;color:var(--muted)}
</style>
</head>
<body>

<header class="abs hero" role="img" aria-label="Close-up photograph of fresh ripe strawberries with green leafy tops"></header>
<div class="abs brand">Plumtree Crate Society</div>
<nav>
  <span class="abs nav" style="left:708px">Home</span>
  <span class="abs nav" style="left:764px">About Us</span>
  <span class="abs nav" style="left:847px">Get Started</span>
</nav>
<div class="abs nav-icons">
  <svg width="15" height="15" viewBox="0 0 16 16" fill="none" stroke="#fff" stroke-width="2"><circle cx="6.5" cy="6.5" r="4.5"/><path d="M10 10l4.5 4.5"/></svg>
  <span style="display:flex;align-items:center;gap:4px"><svg width="14" height="15" viewBox="0 0 14 16" fill="#fff"><path d="M2 5h10l1 10H1z"/><path d="M4.5 5V3.5a2.5 2.5 0 015 0V5" fill="none" stroke="#fff" stroke-width="1.5"/></svg>0</span>
  <svg width="15" height="15" viewBox="0 0 16 16" fill="#fff"><circle cx="8" cy="5" r="3.5"/><path d="M1 15c0-4 3-6 7-6s7 2 7 6z"/></svg>
</div>
<h1 class="abs hero-title">Candy colors will light<br>up daily life</h1>
<a class="abs hero-btn">Get Started</a>

<main>
  <div class="photo tile macarons" style="left:149px;top:626px" role="img" aria-label="Pastel macarons around a cup of black coffee"></div>
  <div class="photo tile pancake" style="left:470px;top:626px" role="img" aria-label="Pancakes with fruit and syrup on a white plate"></div>
  <div class="photo tile cookies" style="left:149px;top:874px" role="img" aria-label="Bowl of sandwich cookies"></div>
  <div class="photo tile citrus" style="left:470px;top:874px" role="img" aria-label="Citrus drink with grapefruit and rosemary"></div>
  <div class="photo tile teacup" style="left:149px;top:1134px" role="img" aria-label="Teacup and saucer on a table with knitted sleeve"></div>
  <div class="photo tile tray" style="left:470px;top:1134px" role="img" aria-label="Breakfast tray with waffles and berries"></div>
  <div class="photo tile drinks" style="left:149px;top:1398px" role="img" aria-label="Red berry cocktails with rosemary"></div>
  <div class="photo tile parfait" style="left:470px;top:1398px" role="img" aria-label="Strawberry yogurt parfaits in jars"></div>

  <aside>
    <div class="abs book" role="img" aria-label="Recipe book cover with a stack of pancakes and berries"></div>
    <div class="abs social-box"><span>Chirp</span><span>Facet</span><span>Snap</span><span>Pinn</span><span>Lovu</span><span>Gleam</span></div>
    <div class="abs cat cakes" role="img" aria-label="Chocolate cupcakes with cream frosting"><span class="cat-label">CAKES</span></div>
    <div class="abs cat fruits" role="img" aria-label="Breakfast tray with fruit and waffles"><span class="cat-label">FRUITS</span></div>
    <div class="abs newsletter">
      <div class="nl-head">NEWSLETTER</div>
      <p class="nl-text">Subscribe to my weekly newsletter.</p>
      <div class="nl-input">Your email address</div>
      <div class="nl-btn">Sign up</div>
    </div>
  </aside>

  <article>
    <div class="photo feature" role="img" aria-label="Pancake topped with cream, strawberries, kiwi and blueberries beside a fork and knife"></div>
    <h2 class="abs post-title">Quick fruits dessert for a summery afternoon</h2>
    <div class="abs post-date">December 4, 2017</div>
    <p class="abs post-excerpt">This was such a new idea to Mabel, that she was quite silent for a minute or two, which gave the Pigeon the opportunity of...</p>
  </article>
</main>

<footer class="abs footer">
  <ul class="f-col" style="left:149px"><li>Brand</li><li>Our Blog</li><li>Press Release</li><li>Other</li></ul>
  <ul class="f-col" style="left:346px"><li>Our Story</li><li>FAQ</li><li>Contact us</li><li>Size Guide</li></ul>
  <ul class="f-col" style="left:529px"><li>Wholesale Inquiries</li><li>Returns &amp; Exchanges</li><li>Affiliate Program</li></ul>
  <ul class="f-col" style="left:747px"><li>My Account</li><li>Payment</li><li>Shipping</li><li>Returns</li></ul>
  <div class="pay">
    <div class="pay-row"><span>Tillo</span><span>Coinra</span><span>Vexo</span><span>Dinra</span></div>
    <div class="pay-row"><span>Findly</span><span>Kobi</span><span>Merro</span></div>
    <div class="pay-row"><span>Pursa</span><span>Zenti</span></div>
  </div>
  <p class="copyright">© 2017, Plumtree Crate Society All Rights Resreved</p>
</footer>

</body>
</html>
```